Agricultural Commodities Specialist Needs a Business Card Design

Business owner Rob Hartwell, need a business card design for his company based in Brisbane, Australia called "RH Tradelink Pty Ltd".
Rob is an Agricultural Commodities Specialist:
-Specialising in Domestic and Export of Cotton,Cottonseed and Grains.
-Extensive experience in exporting into Asia especially China.
-Buyers agent for one of China's largest spinning mills.
-Capital raising from foreign investors into Australian agriculture.
-Agricultural marketing strategies for corporate and family farms.
-Importer of niche products from China.
-Array of contacts in agriculture and manufacturing in China.

Rob would like a professional business card with his company name "RH Tradelink" on the front of his business card - with contact details on the back. Preferably black and white colours.

CONTACT DETAILS THAT NEED TO BE INCLUDED:

Rob Hartwell
Mobile: 0431 275 604

Po Box 518
Elm Vale QLD 4187

Email: rob@rhtradelinkco.com
website: www.rhtradelinkc.com

```html
<!DOCTYPE html>
<html lang="en">
<head>
<meta charset="UTF-8">
<title>RH Tradelink – Business Card</title>
<link href="https://fonts.googleapis.com/css2?family=Cinzel:wght@400;600&display=swap" rel="stylesheet">
<style>
  :root {
    --page: #e8e5e0;
    --card-black: #0d0d0d;
    --card-white: #ffffff;
    --brand-green: #5a9a2c;
    --ink: #1e1e1e;
    --ink-light: #ffffff;
    --sunset-dark: #2c3a4a;
    --sunset-warm: #c9884a;
    --cotton-soil: #7a5a3c;
    --cotton-light: #d9d2c4;
    --crop-green: #4f8a2e;
    --crop-light: #8dbb5a;
  }
  html, body {
    margin: 0;
    padding: 0;
    overflow: hidden;
  }
  body {
    width: 1200px;
    height: 912px;
    background: var(--page);
    font-family: "Cinzel", serif;
  }
  .canvas {
    position: relative;
    width: 1200px;
    height: 912px;
  }
  .card {
    position: absolute;
    left: 240px;
    width: 720px;
    height: 412px;
    border-radius: 6px;
    overflow: hidden;
    box-shadow: 0 10px 28px rgba(0,0,0,0.25);
    background: var(--card-black);
  }
  .card--front { top: 30px; }
  .card--back { top: 470px; }
  .card svg { display: block; }
  .company-name {
    font-family: "Cinzel", serif;
    font-weight: 600;
    font-size: 27px;
    letter-spacing: 2px;
    fill: var(--ink);
  }
  .person-name {
    font-family: "Cinzel", serif;
    font-weight: 600;
    font-size: 23px;
    letter-spacing: 2px;
    fill: var(--ink-light);
  }
  .contact-line {
    font-family: "Cinzel", serif;
    font-weight: 600;
    font-size: 14px;
    letter-spacing: 0.5px;
    fill: var(--ink);
  }
  .icon-box { fill: var(--brand-green); }
  .icon-mark { fill: none; stroke: #fff; stroke-width: 1.6; }
  .icon-solid { fill: #fff; }
</style>
</head>
<body>
<div class="canvas">

  <svg width="0" height="0" style="position:absolute">
    <defs>
      <linearGradient id="sunset-field" x1="0" y1="0" x2="0" y2="1">
        <stop offset="0" stop-color="#6f8fae"/>
        <stop offset="0.45" stop-color="#c9884a"/>
        <stop offset="0.6" stop-color="#2c3a4a"/>
        <stop offset="1" stop-color="#1c2a1e"/>
      </linearGradient>
      <linearGradient id="cotton-field" x1="0" y1="0" x2="1" y2="1">
        <stop offset="0" stop-color="#9fb8cc"/>
        <stop offset="0.35" stop-color="#d9d2c4"/>
        <stop offset="1" stop-color="#7a5a3c"/>
      </linearGradient>
      <linearGradient id="crop-field" x1="0" y1="0" x2="1" y2="1">
        <stop offset="0" stop-color="#8dbb5a"/>
        <stop offset="1" stop-color="#4f8a2e"/>
      </linearGradient>
    </defs>
  </svg>

  <!-- Front of card -->
  <div class="card card--front">
    <svg width="720" height="412" viewBox="0 0 720 412">
      <rect width="720" height="412" fill="var(--card-black)"/>
      <g transform="rotate(-14.78 0 250)">
        <g class="photo-strip">
          <rect x="-60" y="250" width="320" height="87" fill="url(#sunset-field)" role="img" aria-label="Photo of a crop field at sunset"/>
          <rect x="260" y="250" width="250" height="87" fill="url(#cotton-field)" role="img" aria-label="Photo of cotton bales in a field"/>
          <rect x="510" y="250" width="320" height="87" fill="url(#crop-field)" role="img" aria-label="Photo of green crop rows"/>
        </g>
        <rect class="white-band" x="-60" y="337" width="900" height="87" fill="var(--card-white)"/>
        <rect class="green-band" x="-60" y="424" width="900" height="48" fill="var(--brand-green)"/>
        <text class="company-name" x="668" y="390" text-anchor="end">RH Tradelink</text>
      </g>
    </svg>
  </div>

  <!-- Back of card -->
  <div class="card card--back">
    <svg width="720" height="412" viewBox="0 0 720 412">
      <rect width="720" height="412" fill="var(--card-black)"/>
      <g transform="rotate(-14.78 0 250)">
        <g class="photo-strip">
          <rect x="-60" y="250" width="320" height="87" fill="url(#sunset-field)" role="img" aria-label="Photo of a crop field at sunset"/>
          <rect x="260" y="250" width="250" height="87" fill="url(#cotton-field)" role="img" aria-label="Photo of cotton bales in a field"/>
          <rect x="510" y="250" width="320" height="87" fill="url(#crop-field)" role="img" aria-label="Photo of green crop rows"/>
        </g>
        <rect class="white-band" x="-60" y="337" width="900" height="87" fill="var(--card-white)"/>
        <rect class="green-band" x="-60" y="424" width="900" height="48" fill="var(--brand-green)"/>
        <text class="person-name" x="672" y="328" text-anchor="end">Rob Hartwell</text>

        <g class="contact-item" transform="translate(70 352)">
          <rect class="icon-box" width="22" height="22" rx="2"/>
          <rect class="icon-mark" x="4.5" y="6.5" width="13" height="9"/>
          <path class="icon-mark" d="M4.5 6.5 L11 12 L17.5 6.5"/>
          <text class="contact-line" x="32" y="16">rob@rhtradelinkco.com</text>
        </g>
        <g class="contact-item" transform="translate(70 386)">
          <rect class="icon-box" width="22" height="22" rx="2"/>
          <circle class="icon-mark" cx="11" cy="11" r="6.5"/>
          <ellipse class="icon-mark" cx="11" cy="11" rx="2.8" ry="6.5"/>
          <path class="icon-mark" d="M4.5 11 H17.5"/>
          <text class="contact-line" x="32" y="16">www.rhtradelinkc.com</text>
        </g>
        <g class="contact-item" transform="translate(400 348)">
          <rect class="icon-box" width="22" height="22" rx="2"/>
          <path class="icon-solid" d="M11 4 C7.8 4 6 6.2 6 8.8 C6 12 11 18 11 18 C11 18 16 12 16 8.8 C16 6.2 14.2 4 11 4 Z"/>
          <circle cx="11" cy="8.8" r="2" fill="var(--brand-green)"/>
          <text class="contact-line" x="32" y="9">Po Box 518</text>
          <text class="contact-line" x="32" y="26">Elm Vale QLD 4187</text>
        </g>
        <g class="contact-item" transform="translate(400 388)">
          <rect class="icon-box" width="22" height="22" rx="2"/>
          <path class="icon-solid" d="M7 4.5 L9.5 4.5 L10.5 8 L9 9.3 C9.8 11 11 12.2 12.7 13 L14 11.5 L17.5 12.5 L17.5 15 C17.5 16.2 16.5 17.5 15 17.3 C10 16.7 5.3 12 4.7 7 C4.5 5.5 5.8 4.5 7 4.5 Z"/>
          <text class="contact-line" x="32" y="16">0431 275 604</text>
        </g>
      </g>
    </svg>
  </div>

</div>
</body>
</html>
```